Elegant Business Cards & Letterhead

We will need the following that need to be designed: Letterhead and Business Cards, there winer will be re-hired for the balance of our stationary needs. Text for the cards and letterheads:

- Corporate Card instead of name
- landline: +971 (4) 362 7041
- mobile: +971 56 2819 605
- 800TUTOR
- email: dubai@velmora-lune.com
- www.velmora-lune.com
- PO Box 387261
Address: Castellan Heights Suite 1708, Dubai UAE

Thank you

Target Market(s)

VIPs, HNWI, High-end Families.

Industry/Entity Type

Luxury Market

Font styles to use
Other font styles liked:
• as explained

Colors

Designer to choose only greyscale colors for use in the design.

Requirements
Must have
• Elegant, Simple, Luxurious, Minimalistic
Nice to have
• Luxury, Golds, Engravings,
Should not have
• Much colors, funky,

```html
<!DOCTYPE html>
<html lang="en">
<head>
<meta charset="UTF-8">
<title>Velmora Lune — Stationery</title>
<link href="https://fonts.googleapis.com/css2?family=Arimo:wght@400;700&family=Marcellus&display=swap" rel="stylesheet">
<style>
  :root {
    --backdrop: #6b6c6e;
    --card: #2e2e2f;
    --card-deep: #2a2a2b;
    --card-text: #e9e9e9;
    --logo-card: #a9a9a9;
    --paper: #ffffff;
    --ink: #111111;
    --ink-soft: #555555;
    --body-text: #6a6a6a;
  }
  * { margin: 0; padding: 0; box-sizing: border-box; }
  html, body { width: 1200px; height: 1091px; overflow: hidden; }
  body {
    background: var(--backdrop);
    font-family: "Arimo", Arial, sans-serif;
    position: relative;
  }
  .brand {
    font-family: "Marcellus", serif;
    letter-spacing: 0.02em;
    white-space: nowrap;
  }

  /* Business cards */
  .card {
    position: absolute;
    width: 360px;
    height: 205px;
    border-radius: 12px;
    background: var(--card);
    box-shadow: 2px 2px 2px rgba(0,0,0,0.25);
  }
  .card--front { left: 124px; top: 317px; }
  .card--back { left: 122px; top: 551px; background: var(--card-deep); }

  .card__brand {
    position: absolute;
    left: 41px; top: 92px;
    font-size: 17px;
    color: var(--logo-card);
  }
  .card__divider {
    position: absolute;
    left: 188px; top: 43px;
    width: 1px; height: 119px;
    background: linear-gradient(to bottom, transparent, #cfcfcf 30%, #cfcfcf 70%, transparent);
  }
  .card__details {
    position: absolute;
    left: 205px; top: 57px;
    color: var(--card-text);
    font-size: 8.6px;
    line-height: 10.4px;
  }
  .card__address { margin-bottom: 6px; }
  .contact-row { display: flex; align-items: center; gap: 6px; }
  .contact-row svg { width: 7px; height: 7px; fill: currentColor; flex: none; }

  .card--back .card__brand {
    left: 0; right: 0; top: 86px;
    text-align: center;
    font-size: 26px;
    color: #8f8f8f;
  }

  /* Letterhead */
  .letterhead {
    position: absolute;
    left: 513px; top: 146px;
    width: 580px; height: 815px;
    background: var(--paper);
    box-shadow: 2px 2px 3px rgba(0,0,0,0.3);
  }
  .letterhead__brand {
    position: absolute;
    left: 0; right: 0; top: 70px;
    text-align: center;
    font-size: 27px;
    color: var(--ink);
  }
  .recipient {
    position: absolute;
    left: 60px; top: 193px;
    font-size: 10px;
    line-height: 11.7px;
    color: var(--ink);
  }
  .salutation {
    position: absolute;
    left: 59px; top: 329px;
    font-size: 10.5px;
    font-weight: 700;
    color: var(--ink-soft);
  }
  .letter-body {
    position: absolute;
    left: 59px; top: 368px;
    width: 465px;
    font-size: 9.3px;
    line-height: 10.4px;
    color: var(--body-text);
  }
  .letter-body p { margin-bottom: 10.4px; }
  .signature {
    position: absolute;
    left: 61px; top: 609px;
    color: var(--ink-soft);
    font-size: 11px;
    line-height: 13px;
  }
  .signature__name { font-weight: 700; }

  .letter-footer {
    position: absolute;
    left: 63px; top: 752px;
    width: 452px;
    color: var(--ink);
    font-size: 7.6px;
    text-align: center;
  }
  .letter-footer__address {
    padding-bottom: 3px;
    border-bottom: 1px solid var(--ink);
  }
  .letter-footer__contacts {
    display: flex;
    justify-content: center;
    gap: 6px;
    margin-top: 6px;
    padding-left: 10px;
  }
  .letter-footer__contacts .contact-row { gap: 5px; }
</style>
</head>
<body>

<svg width="0" height="0" style="position:absolute">
  <defs>
    <symbol id="icon-phone" viewBox="0 0 10 10"><path d="M2 0.5 L3.6 2.6 L2.8 3.6 C3.4 5 4.8 6.4 6.3 7.1 L7.3 6.3 L9.5 7.9 L8.5 9.5 C4.5 9.3 0.6 5.4 0.4 1.5 Z"/></symbol>
    <symbol id="icon-mobile" viewBox="0 0 10 10"><path d="M2.5 0 H7.5 V10 H2.5 Z M3.4 1 V8.3 H6.6 V1 Z"/></symbol>
    <symbol id="icon-mail" viewBox="0 0 10 10"><path d="M0 2 H10 V8.5 H0 Z M0.8 2.6 L5 5.7 L9.2 2.6 Z"/></symbol>
    <symbol id="icon-globe" viewBox="0 0 10 10"><path d="M5 0 A5 5 0 1 0 5 10 A5 5 0 1 0 5 0 Z M2.5 2.5 L4.5 2 L5 3.5 L3.5 4.5 L4 6.5 L2.5 7.5 L1.5 5 Z M6 5 L8.5 5.5 L7.5 8 L6 7 Z"/></symbol>
  </defs>
</svg>

<section class="card card--front" aria-label="Business card front">
  <div class="card__brand brand">VELMORA LUNE</div>
  <div class="card__divider"></div>
  <div class="card__details">
    <div class="card__address">
      PO Box 387261<br>
      Castellan Heights<br>
      Suite 1708, Dubai UAE
    </div>
    <div class="contact-row"><svg><use href="#icon-phone"/></svg>+971 (4) 362 7041</div>
    <div class="contact-row"><svg><use href="#icon-mobile"/></svg>+971 56 2819 605</div>
    <div class="contact-row"><svg><use href="#icon-phone"/></svg>800TUTOR</div>
    <div class="contact-row"><svg><use href="#icon-mail"/></svg>dubai@velmora-lune.com</div>
    <div class="contact-row"><svg><use href="#icon-globe"/></svg>www.velmora-lune.com</div>
  </div>
</section>

<section class="card card--back" aria-label="Business card back">
  <div class="card__brand brand">VELMORA LUNE</div>
</section>

<section class="letterhead" aria-label="Letterhead">
  <div class="letterhead__brand brand">VELMORA LUNE</div>

  <div class="recipient">
    Anrede<br>Name<br>Straße<br>PLZ und ORT
  </div>

  <div class="salutation">Dear Sir</div>

  <div class="letter-body">
    <p>Lorem ipsum dolor sit amet. Non quam iste ut dolor repellendus aut quasi porro nam molestias ullam ut sint ipsa! Qui accusamus assumenda qui quae tempore sit quia velit aut porro tempora. Est iste explicabo aut alias impedit est sequi quis.</p>
    <p>Cum rerum molestiae id galisum odit et autem voluptas aut blanditiis iste ut aspernatur itaque ut tempora laudantium vel voluptatem repudiandae! Ea delectus omnis est voluptas odit ut assumenda quisquam eos facere sunt qui quis vitae. Qui velit dolorem in distinctio</p>
    <p>dignissimos rem voluptatem totam ut quia nostrum cum quas consequuntur. Quo aliquid earum eum optio ducimus qui fugiat veniam qui blanditiis velit ut quos dolores non officiis enim ut voluptatem veritatis.</p>
    <p>At quia sunt nam quibusdam mollitia aut rerum laudantium et inventore molestiae aut cumque consequa­tur. 33 minima velit rem quasi galisum ut quae magni sed praesentium possimus 33 commodi quam qui quae aperiam est enim accusantium. Sed Quis laboriosam ut suscipit maxime cum reprehenderit adipisci. Non nihil dolor ut obcaecati commodi aut Quis provident eos doloribus cumque.</p>
    <p>At quia sunt nam quibusdam mollitia aut rerum laudantium et inventore molestiae aut cumque consequa­tur. 33 minima velit rem quasi galisum ut quae</p>
  </div>

  <div class="signature">
    <div class="signature__name">ADRIAN KESSLER</div>
    <div>Geschäftsführer</div>
  </div>

  <footer class="letter-footer">
    <div class="letter-footer__address">PO Box 387261, Castellan Heights, Suite 1708, Dubai UAE</div>
    <div class="letter-footer__contacts">
      <span class="contact-row"><svg><use href="#icon-phone"/></svg>+971 (4) 362 7041</span>
      <span class="contact-row"><svg><use href="#icon-phone"/></svg>800TUTOR</span>
      <span class="contact-row"><svg><use href="#icon-mail"/></svg>dubai@velmora-lune.com</span>
      <span class="contact-row"><svg><use href="#icon-globe"/></svg>www.velmora-lune.com</span>
    </div>
  </footer>
</section>

</body>
</html>
```